Legal Service Estimated Retainer and Average Case Value

We need an 11x14 flyer that contains the standard retainers and average cost be case, both provided in documents, for each case type we handle. We need the information displayed, preferably in a way that makes the information readable but less troubling to a client shocked at price of litigation. We need one sheet with the retainers and average case value merged into one table.

Target Market(s)

Potential Clients

Font styles to use
Serif
Sans Serif

```html
<!DOCTYPE html>
<html lang="en">
<head>
<meta charset="utf-8">
<title>Average Fees and Retainers</title>
<link href="https://fonts.googleapis.com/css2?family=Cinzel:wght@700&family=Poppins:wght@400;500&family=Tinos&display=swap" rel="stylesheet">
<style>
  :root {
    --navy: #1d2a5c;
    --row-dark: #1b2257;
    --row-light: #3d53a5;
    --ink: #1a1a1a;
    --sky: #c9dcef;
    --sky-soft: #eef4fb;
    --ribbon: #c8171e;
    --brass: #b8923a;
    --white: #ffffff;
  }
  * { margin: 0; padding: 0; box-sizing: border-box; }
  html, body { width: 943px; height: 1200px; overflow: hidden; background: var(--white); }
  .flyer { position: relative; width: 943px; height: 1200px; overflow: hidden; background: var(--white); }

  .sky-backdrop {
    position: absolute; inset: 0 0 auto 0; height: 760px;
    background:
      radial-gradient(ellipse 420px 300px at 860px 120px, var(--sky) 0%, rgba(201,220,239,0) 100%),
      radial-gradient(ellipse 520px 260px at 200px 120px, var(--sky-soft) 0%, rgba(238,244,251,0) 100%),
      linear-gradient(180deg, #e4eef8 0%, rgba(255,255,255,0) 100%);
  }
  .ribbon-accent {
    position: absolute; left: 0; top: 0; width: 300px; height: 60px;
    background: linear-gradient(100deg, var(--ribbon) 0%, #e0353a 55%, rgba(224,53,58,0) 100%);
    border-radius: 0 0 60% 0 / 0 0 100% 0;
  }
  .scales-accent {
    position: absolute; right: 0; top: 800px; width: 50px; height: 400px;
    background: linear-gradient(90deg, rgba(184,146,58,0) 0%, rgba(184,146,58,0.45) 100%);
  }
  .book-accent {
    position: absolute; left: 0; bottom: 0; width: 943px; height: 34px;
    background: linear-gradient(180deg, rgba(255,255,255,0) 0%, #e9dcc0 60%, #c9ab78 100%);
  }

  .firm-mark {
    position: absolute; left: 306px; top: 52px; width: 30px; height: 30px;
    background: var(--navy);
  }
  .firm-name {
    position: absolute; left: 350px; top: 46px;
    font-family: 'Cinzel', serif; font-weight: 700; color: var(--navy);
    line-height: 1; text-transform: uppercase;
  }
  .firm-name .prefix { display: block; font-size: 15px; margin-bottom: 6px; }
  .firm-name .name { display: block; font-size: 34px; }

  .intro {
    position: absolute; left: 0; top: 143px; width: 943px;
    font-family: 'Tinos', serif; font-size: 20.5px; line-height: 24.5px;
    color: var(--ink); text-align: center; white-space: nowrap;
  }

  .section-title {
    position: absolute; left: 0; top: 256px; width: 943px; text-align: center;
    font-family: 'Cinzel', serif; font-weight: 700; font-size: 22px;
    color: var(--navy); text-transform: uppercase; letter-spacing: 0.5px;
  }

  .rate-table { position: absolute; left: 56px; top: 296px; width: 830px; }
  .rate-row { display: flex; gap: 5px; margin-bottom: 6px; }
  .rate-row > div { white-space: nowrap; }
  .rate-row .case { flex: 1; padding-left: 18px; }
  .rate-row .fee { width: 170px; padding-left: 14px; }
  .rate-row .retainer { width: 180px; padding-left: 14px; }

  .rate-head > div {
    height: 30px; line-height: 30px;
    font-family: 'Cinzel', serif; font-weight: 700; font-size: 15px;
    color: var(--navy); text-transform: uppercase;
    border-bottom: 2px solid var(--navy);
  }
  .rate-body > div {
    height: 46px; line-height: 46px;
    background: linear-gradient(90deg, var(--row-dark), var(--row-light));
    color: var(--white); font-family: 'Poppins', sans-serif; font-weight: 400;
    font-size: 16.5px;
  }
</style>
</head>
<body>
<div class="flyer">
  <div class="sky-backdrop" role="img" aria-label="Soft blue sky with clouds and white doves"></div>
  <div class="ribbon-accent" role="img" aria-label="Red ribbon flowing across the top corner"></div>
  <div class="scales-accent" role="img" aria-label="Brass scales of justice"></div>
  <div class="book-accent" role="img" aria-label="Law book and gavel along the bottom edge"></div>

  <div class="firm-mark"></div>
  <div class="firm-name">
    <span class="prefix">The Law Office of</span>
    <span class="name">Marcus T Holloway</span>
  </div>

  <p class="intro">In order for our clients to set expectations for legal fees, we provide the national average range<br>of fees per case type. These are only to provide you with an understanding of what other cases<br>have cost clients in similar cases. Please note these are not estimates nor guarantees<br>of your own legal costs.</p>

  <h2 class="section-title">Average Fee and Retainer Per Case Type</h2>
  <div class="rate-table">
    <div class="rate-row rate-head"><div class="case">Case Type</div><div class="fee">Average Fee</div><div class="retainer">Retainer</div></div>
    <div class="rate-row rate-body"><div class="case">Custody Contempt/Modification</div><div class="fee">$5,000 - $8,000</div><div class="retainer">$3,500</div></div>
    <div class="rate-row rate-body"><div class="case">Custody Initial Order</div><div class="fee">$4,000 - $7,000</div><div class="retainer">$3,000</div></div>
    <div class="rate-row rate-body"><div class="case">Custody &amp; Support</div><div class="fee">$5,000 - $8,000</div><div class="retainer">$3,000</div></div>
    <div class="rate-row rate-body"><div class="case">Support</div><div class="fee">$2,000 - $4,000</div><div class="retainer">&mdash;</div></div>
    <div class="rate-row rate-body"><div class="case">Divorce (3301c)</div><div class="fee">$1,500 - $3,000</div><div class="retainer">$2,000</div></div>
    <div class="rate-row rate-body"><div class="case">Divorce (3301d)</div><div class="fee">$2,000 - $3,000</div><div class="retainer">$2,500</div></div>
    <div class="rate-row rate-body"><div class="case">(PFA) Protection from Abuse</div><div class="fee">$1,500 - $3,000</div><div class="retainer">$2,000 Paid In Full</div></div>
    <div class="rate-row rate-body"><div class="case">Divorce &amp; Custody</div><div class="fee">$5,000 - $8,000</div><div class="retainer">$3,500</div></div>
    <div class="rate-row rate-body"><div class="case">Divorce &amp; Support</div><div class="fee">&mdash;</div><div class="retainer">$3,000</div></div>
    <div class="rate-row rate-body"><div class="case">Divorce &amp; Equitable Distribution</div><div class="fee">$6,000 - $10,000</div><div class="retainer">$3,500</div></div>
    <div class="rate-row rate-body"><div class="case">Divorce, Custody &amp; Support</div><div class="fee">$8,000 - $12,000</div><div class="retainer">$3,500</div></div>
    <div class="rate-row rate-body"><div class="case">Divorce, Equitable Distribution &amp; Custody</div><div class="fee">$10,000 - $15,000</div><div class="retainer">$5,000</div></div>
    <div class="rate-row rate-body"><div class="case">Divorce, Equitable Distribution &amp; Support</div><div class="fee">$8,000 - $12,000</div><div class="retainer">$3,500</div></div>
    <div class="rate-row rate-body"><div class="case">Divorce, Equitable Distribution, Custody &amp; Support</div><div class="fee">$12,000 - $15,000</div><div class="retainer">$3,500</div></div>
  </div>
</div>
</body>
</html>
```